Redesign Comparisson chart - make modern and effective

Use your imaginations to make a powerful distinction between KRV & other holistic modalities. There are 7 elements physical, mental, emotional, energetic, subconscious, superconscious and before and after testing.
We want it to be obvious that KRV is the only modality that works on all these elements simultaneously. We do not want to include any chakras as we want this information to be accepted by a wide range of people and belief systems.'

We want it to look simple but effective. Professional but powerful. We want KRV to stand out even of you eye just passed over i.
Updates

Hi everyone, thanks for your submissions so far. Basically what this image is meant to represent is a comparison chart between all the modalities There are 5 elements physical, mental, emotional, subconscious and superconscious. we want to reflect that KRV is the only modality that works on all these elements simultaneously. As we want the concept to be accepted and not considered woo woo, we want to steer away from chakras.

Target Market(s)

Professionals

Industry/Entity Type

Professional services

Font styles to use
Sans Serif
Other font styles liked:
• Poppins Monserratt

Colors
0094D4
00A9DD
6FCCEA
C7EBF8
E9F6FB

Requirements
Must have
• Clear/professional and clean look. Brand colours and logos. All typography and formats must be cohesive.
Nice to have
• More easy to read, different layout
Should not have
• Do not change the data just the way its presented. No chakras

```html
<!DOCTYPE html>
<html lang="en">
<head>
<meta charset="utf-8">
<title>KRV – Healing Modalities Comparison</title>
<link rel="stylesheet" href="https://fonts.googleapis.com/css2?family=Montserrat:ital,wght@1,900&family=Oswald:wght@500;700&family=Poppins:wght@400;600&display=swap">
<style>
  :root{
    --page:#cccccc;
    --paper:#ffffff;
    --cell:#e2e8f8;
    --label-ring:#f9b51a;
    --hero:#4a4a4a;
    --navy:#1d2d6b;
    --heading:#3a4a8c;
    --ink:#2b2b2b;
    --physical:#f37321;
    --mental:#cc004c;
    --emotional:#77808a;
    --energetic:#6761ab;
    --subconscious:#0288d1;
    --superconscious:#0db14b;
    --testing:#06612e;
    --brand:#35b8e8;
  }
  html,body{margin:0;padding:0;width:745px;height:1200px;overflow:hidden;background:var(--page);}
  .canvas{position:relative;width:745px;height:1200px;overflow:hidden;background:var(--page);font-family:"Poppins",sans-serif;}
  .arch{position:absolute;left:36px;top:38px;width:669px;height:1123px;background:var(--paper);border-radius:334px 334px 0 0;}

  .wheel{position:absolute;left:0;top:0;width:745px;height:700px;}
  .ring{fill:none;stroke:var(--cell);stroke-width:21;stroke-dasharray:12.4 1.446;}
  .ring.labels{stroke:var(--label-ring);stroke-width:46;}
  .cell{fill:none;stroke-width:21;stroke-dasharray:12.4 347.6;}
  .cell.hero{stroke:var(--hero);stroke-width:46;}
  .physical{stroke:var(--physical);stroke-width:22;}
  .physical.off-tone{stroke:var(--label-ring);}
  .mental{stroke:var(--mental);}
  .emotional{stroke:var(--emotional);}
  .energetic{stroke:var(--energetic);}
  .subconscious{stroke:var(--subconscious);}
  .superconscious{stroke:var(--superconscious);}
  .testing{stroke:var(--testing);}
  .modality{font-family:"Oswald",sans-serif;font-weight:500;font-size:9.5px;fill:var(--navy);text-anchor:middle;}
  .modality.small{font-size:8.4px;}
  .hero-name{font-family:"Poppins",sans-serif;font-weight:600;font-size:20px;fill:#fff;text-anchor:middle;}
  .spoke-icon{color:#fff;}
  .center-mark{fill:var(--brand);}
  .center-name{font-family:"Poppins",sans-serif;font-weight:600;font-size:27px;fill:var(--brand);text-anchor:middle;}

  .brand-row{position:absolute;left:75px;top:670px;height:56px;display:flex;align-items:center;}
  .brand-dot{width:55px;height:55px;border-radius:50%;background:var(--brand);}
  .brand-name{margin-left:10px;font-weight:600;font-size:30px;color:var(--brand);letter-spacing:.5px;}
  .divider{position:absolute;left:228px;top:680px;height:44px;border-left:1.5px dotted #8a8fa8;}
  .claim{position:absolute;left:240px;top:690px;margin:0;font-family:"Oswald",sans-serif;font-weight:700;font-style:italic;font-size:19px;line-height:19px;color:var(--heading);letter-spacing:.2px;}
  .statements{position:absolute;left:74px;top:736px;margin:0;padding:0;list-style:none;font-size:12.6px;line-height:17.5px;color:var(--ink);}

  .card{position:absolute;box-sizing:border-box;border:1.5px solid;border-radius:5px;background:#fff;}
  .card .tab{position:absolute;left:-1.5px;top:-1.5px;width:44px;height:42px;border-radius:5px 0 42px 0;display:flex;align-items:center;justify-content:center;color:#fff;}
  .card .tab svg{width:24px;height:24px;margin:-4px 4px 0 0;}
  .card h2{position:absolute;left:45px;top:9px;margin:0;font-family:"Montserrat",sans-serif;font-weight:900;font-style:italic;font-size:16px;line-height:18px;letter-spacing:.3px;text-transform:uppercase;}
  .card h2.compact{font-size:14.2px;}
  .card p{position:absolute;left:45px;top:30px;width:243px;margin:0;font-size:8.3px;line-height:11.5px;color:var(--ink);}
  .card.physical-card{border-color:var(--physical);} .physical-card .tab{background:var(--physical);} .physical-card h2{color:var(--physical);}
  .card.mental-card{border-color:var(--mental);} .mental-card .tab{background:var(--mental);} .mental-card h2{color:var(--mental);}
  .card.emotional-card{border-color:var(--emotional);} .emotional-card .tab{background:var(--emotional);} .emotional-card h2{color:var(--emotional);}
  .card.energetic-card{border-color:var(--energetic);} .energetic-card .tab{background:var(--energetic);} .energetic-card h2{color:var(--energetic);}
  .card.subconscious-card{border-color:var(--subconscious);} .subconscious-card .tab{background:var(--subconscious);} .subconscious-card h2{color:var(--subconscious);}
  .card.superconscious-card{border-color:var(--superconscious);} .superconscious-card .tab{background:var(--superconscious);} .superconscious-card h2{color:var(--superconscious);}
  .card.testing-card{border-color:var(--testing);} .testing-card .tab{background:var(--testing);} .testing-card h2{color:var(--testing);}
  .card.contact-card{border-color:var(--brand);text-align:center;}
  .contact-card .contact-brand{position:absolute;left:0;right:0;top:14px;display:flex;justify-content:center;align-items:center;}
  .contact-card .contact-dot{width:26px;height:26px;border-radius:50%;background:var(--brand);}
  .contact-card .contact-name{margin-left:10px;font-weight:600;font-size:17px;color:var(--brand);}
  .contact-card .web{position:absolute;left:0;right:0;top:44px;font-size:18px;color:var(--brand);letter-spacing:.2px;}
</style>
</head>
<body>
<div class="canvas">
  <div class="arch"></div>

  <svg width="0" height="0" style="position:absolute">
    <defs>
      <symbol id="icon-physical" viewBox="0 0 24 24"><g fill="none" stroke="currentColor" stroke-width="1.8" stroke-linecap="round" stroke-linejoin="round"><circle cx="12" cy="4.5" r="2.5"/><path d="M12 8v6M6 12.5l6-2.5 6 2.5M7 15l5-1 5 1M4 19h16M8 15l-3 4M16 15l3 4"/></g></symbol>
      <symbol id="icon-mental" viewBox="0 0 24 24"><g fill="none" stroke="currentColor" stroke-width="1.8" stroke-linecap="round" stroke-linejoin="round"><path d="M8 21v-4a7.5 7.5 0 1 1 10-3l1.5 3h-2.5v4h-4"/><circle cx="12" cy="9.5" r="2.5"/><path d="M15.5 6.5l1.2 1.2 2.3-2.6"/></g></symbol>
      <symbol id="icon-emotional" viewBox="0 0 24 24"><g fill="none" stroke="currentColor" stroke-width="1.8" stroke-linecap="round"><circle cx="7.5" cy="14" r="4.5"/><circle cx="16.5" cy="14" r="4.5"/><path d="M12 2.5v2.5M8 4l1 1.8M16 4l-1 1.8M6 15.5q1.5 1.2 3 0M15 15.5q1.5 1.2 3 0"/></g></symbol>
      <symbol id="icon-energetic" viewBox="0 0 24 24"><g fill="none" stroke="currentColor" stroke-width="1.8" stroke-linecap="round" stroke-linejoin="round"><path d="M13.5 4L8.5 13h4.5l-2 7 5.5-9.5H12z"/><path d="M3 12h2M19 12h2M5.5 5.5l1.4 1.4M17.1 17.1l1.4 1.4M18.5 5.5l-1.4 1.4M6.9 17.1l-1.4 1.4"/></g></symbol>
      <symbol id="icon-subconscious" viewBox="0 0 24 24"><g fill="none" stroke="currentColor" stroke-width="1.8" stroke-linecap="round" stroke-linejoin="round"><circle cx="4" cy="5" r="2"/><path d="M4 7v12M4 15h2M4 18h2"/><path d="M10 21v-4a6.5 6.5 0 1 1 9-2.5l1.5 2.5h-2v4h-3.5"/><circle cx="14.5" cy="9.5" r="2"/><path d="M14.5 11.5v2"/></g></symbol>
      <symbol id="icon-superconscious" viewBox="0 0 24 24"><g fill="none" stroke="currentColor" stroke-width="1.8" stroke-linecap="round" stroke-linejoin="round"><path d="M9 21v-3.5a6 6 0 1 1 7-1l1.5 2.5h-2v2"/><path d="M13 8l-2 4h3l-2 4"/><path d="M12 1.5v2M4.5 5l1.5 1.5M19.5 5L18 6.5M2 11h2M20 11h2"/></g></symbol>
      <symbol id="icon-testing" viewBox="0 0 24 24"><g fill="none" stroke="currentColor" stroke-width="2" stroke-linecap="round"><circle cx="10" cy="10" r="6.5"/><path d="M15 15l6 6"/><path d="M7.5 10.5l2 2 3.5-4"/></g></symbol>
    </defs>
  </svg>

  <svg class="wheel" viewBox="0 0 745 700" role="img" aria-label="Comparison wheel of healing modalities across seven elements">
    <g transform="translate(372 379)">
      <!-- base rings -->
      <circle class="ring labels" r="272" pathLength="360" transform="rotate(-96.2)"/>
      <circle class="ring" r="237.5" pathLength="360" transform="rotate(-96.2)" style="stroke-width:22"/>
      <circle class="ring" r="214.5" pathLength="360" transform="rotate(-96.2)"/>
      <circle class="ring" r="191" pathLength="360" transform="rotate(-96.2)"/>
      <circle class="ring" r="168" pathLength="360" transform="rotate(-96.2)"/>
      <circle class="ring" r="144.5" pathLength="360" transform="rotate(-96.2)"/>
      <circle class="ring" r="121" pathLength="360" transform="rotate(-96.2)"/>
      <circle class="ring" r="97.5" pathLength="360" transform="rotate(-96.2)"/>

      <!-- KRV spoke: every element -->
      <circle class="cell hero" r="272" pathLength="360" transform="rotate(-96.2)"/>
      <circle class="cell physical" r="237.5" pathLength="360" transform="rotate(-96.2)"/>
      <circle class="cell mental" r="214.5" pathLength="360" transform="rotate(-96.2)"/>
      <circle class="cell emotional" r="191" pathLength="360" transform="rotate(-96.2)"/>
      <circle class="cell energetic" r="168" pathLength="360" transform="rotate(-96.2)"/>
      <circle class="cell subconscious" r="144.5" pathLength="360" transform="rotate(-96.2)"/>
      <circle class="cell superconscious" r="121" pathLength="360" transform="rotate(-96.2)"/>
      <circle class="cell testing" r="97.5" pathLength="360" transform="rotate(-96.2)"/>

      <!-- physical -->
      <circle class="cell physical" r="237.5" pathLength="360" transform="rotate(-82.35)"/>
      <circle class="cell physical" r="237.5" pathLength="360" transform="rotate(-68.51)"/>
      <circle class="cell physical" r="237.5" pathLength="360" transform="rotate(-54.66)"/>
      <circle class="cell physical" r="237.5" pathLength="360" transform="rotate(-40.82)"/>
      <circle class="cell physical" r="237.5" pathLength="360" transform="rotate(-26.97)"/>
      <circle class="cell physical" r="237.5" pathLength="360" transform="rotate(-13.12)"/>
      <circle class="cell physical" r="237.5" pathLength="360" transform="rotate(0.72)"/>
      <circle class="cell physical off-tone" r="237.5" pathLength="360" transform="rotate(28.41)"/>
      <circle class="cell physical" r="237.5" pathLength="360" transform="rotate(97.64)"/>
      <circle class="cell physical" r="237.5" pathLength="360" transform="rotate(139.18)"/>
      <circle class="cell physical" r="237.5" pathLength="360" transform="rotate(194.57)"/>
      <circle class="cell physical" r="237.5" pathLength="360" transform="rotate(208.41)"/>
      <circle class="cell physical" r="237.5" pathLength="360" transform="rotate(222.26)"/>
      <circle class="cell physical" r="237.5" pathLength="360" transform="rotate(236.10)"/>
      <circle class="cell physical" r="237.5" pathLength="360" transform="rotate(249.95)"/>

      <!-- mental -->
      <circle class="cell mental" r="214.5" pathLength="360" transform="rotate(14.57)"/>
      <circle class="cell mental" r="214.5" pathLength="360" transform="rotate(42.26)"/>
      <circle class="cell mental" r="214.5" pathLength="360" transform="rotate(56.11)"/>
      <circle class="cell mental" r="214.5" pathLength="360" transform="rotate(125.34)"/>
      <circle class="cell mental" r="214.5" pathLength="360" transform="rotate(153.03)"/>
      <circle class="cell mental" r="214.5" pathLength="360" transform="rotate(166.87)"/>
      <circle class="cell mental" r="214.5" pathLength="360" transform="rotate(194.57)"/>
      <circle class="cell mental" r="214.5" pathLength="360" transform="rotate(208.41)"/>
      <circle class="cell mental" r="214.5" pathLength="360" transform="rotate(222.26)"/>

      <!-- energetic -->
      <circle class="cell energetic" r="168" pathLength="360" transform="rotate(-54.66)"/>
      <circle class="cell energetic" r="168" pathLength="360" transform="rotate(-40.82)"/>
      <circle class="cell energetic" r="168" pathLength="360" transform="rotate(69.95)"/>
      <circle class="cell energetic" r="168" pathLength="360" transform="rotate(83.80)"/>
      <circle class="cell energetic" r="168" pathLength="360" transform="rotate(111.49)"/>
      <circle class="cell energetic" r="168" pathLength="360" transform="rotate(139.18)"/>
      <circle class="cell energetic" r="168" pathLength="360" transform="rotate(208.41)"/>

      <!-- subconscious -->
      <circle class="cell subconscious" r="144.5" pathLength="360" transform="rotate(-26.97)"/>
      <circle class="cell subconscious" r="144.5" pathLength="360" transform="rotate(56.11)"/>
      <circle class="cell subconscious" r="144.5" pathLength="360" transform="rotate(97.64)"/>
      <circle class="cell subconscious" r="144.5" pathLength="360" transform="rotate(125.34)"/>
      <circle class="cell subconscious" r="144.5" pathLength="360" transform="rotate(153.03)"/>
      <circle class="cell subconscious" r="144.5" pathLength="360" transform="rotate(166.87)"/>
      <circle class="cell subconscious" r="144.5" pathLength="360" transform="rotate(180.72)"/>
      <circle class="cell subconscious" r="144.5" pathLength="360" transform="rotate(194.57)"/>

      <!-- superconscious -->
      <circle class="cell superconscious" r="121" pathLength="360" transform="rotate(180.72)"/>

      <!-- before & after testing -->
      <circle class="cell testing" r="97.5" pathLength="360" transform="rotate(-54.66)"/>
      <circle class="cell testing" r="97.5" pathLength="360" transform="rotate(-40.82)"/>
      <circle class="cell testing" r="97.5" pathLength="360" transform="rotate(-26.97)"/>
      <circle class="cell testing" r="97.5" pathLength="360" transform="rotate(0.72)"/>
      <circle class="cell testing" r="97.5" pathLength="360" transform="rotate(56.11)"/>
      <circle class="cell testing" r="97.5" pathLength="360" transform="rotate(97.64)"/>
      <circle class="cell testing" r="97.5" pathLength="360" transform="rotate(111.49)"/>
      <circle class="cell testing" r="97.5" pathLength="360" transform="rotate(153.03)"/>
      <circle class="cell testing" r="97.5" pathLength="360" transform="rotate(194.57)"/>
    </g>

    <!-- spoke icons -->
    <g class="spoke-icon">
      <use href="#icon-physical" x="365" y="134.5" width="14" height="14"/>
      <use href="#icon-mental" x="365" y="157.5" width="14" height="14"/>
      <use href="#icon-emotional" x="365" y="181" width="14" height="14"/>
      <use href="#icon-energetic" x="365" y="204" width="14" height="14"/>
      <use href="#icon-subconscious" x="365" y="227.5" width="14" height="14"/>
      <use href="#icon-superconscious" x="365" y="251" width="14" height="14"/>
      <use href="#icon-testing" x="365" y="274.5" width="14" height="14"/>
    </g>

    <!-- modality labels -->
    <text class="hero-name" x="372" y="114">KRV</text>
    <text class="modality" x="437.1" y="118.5">MASSAGE</text>
    <text class="modality" x="498.4" y="141.7">YOGA</text>
    <text class="modality"><tspan x="552.4" y="173.3">CHINESE</tspan><tspan x="552.4" y="184.8">MEDICINE</tspan></text>
    <text class="modality" x="595.9" y="228.1">CHIROPRACTIC</text>
    <text class="modality" x="626.3" y="286.2">KINESIOLOGY</text>
    <text class="modality" x="642" y="349.8">NATROPATHY</text>
    <text class="modality"><tspan x="642" y="409.7">NUTRITIONAL</tspan><tspan x="642" y="421.2">HEALING</tspan></text>
    <text class="modality" x="626.3" y="479.1">PSHYCHOLOGY</text>
    <text class="modality small"><tspan x="595.9" y="531.4">MINDFULNESS</tspan><tspan x="595.9" y="542.4">MEDITATION</tspan></text>
    <text class="modality"><tspan x="552.4" y="580.5">LIFE</tspan><tspan x="552.4" y="592">COACHING</tspan></text>
    <text class="modality" x="498.4" y="623.5">NLP</text>
    <text class="modality" x="437.1" y="646.7">REIKI</text>
    <text class="modality"><tspan x="372" y="648.9">CRYSTAL</tspan><tspan x="372" y="660.4">HEALING</tspan></text>
    <text class="modality"><tspan x="306.9" y="641">BOWEN</tspan><tspan x="306.9" y="652.5">THERAPY</tspan></text>
    <text class="modality"><tspan x="245.6" y="617.8">ENERGY</tspan><tspan x="245.6" y="629.3">MEDICINE</tspan></text>
    <text class="modality" x="191.6" y="586.2">HYPNOTHERAPY</text>
    <text class="modality" x="148.1" y="537.1">ACCUPUNTURE</text>
    <text class="modality"><tspan x="117.7" y="473.4">TIMELINE</tspan><tspan x="117.7" y="484.9">THERAPY</tspan></text>
    <text class="modality"><tspan x="102" y="404">INNER</tspan><tspan x="102" y="415.4">CHILD</tspan><tspan x="102" y="426.9">HEALING</tspan></text>
    <text class="modality"><tspan x="102" y="344.1">THETA</tspan><tspan x="102" y="355.6">HEALING</tspan></text>
    <text class="modality" x="117.7" y="286.2">EFT</text>
    <text class="modality small"><tspan x="148.1" y="222.4">FAMILY</tspan><tspan x="148.1" y="233.4">CONSTELLATION</tspan></text>
    <text class="modality"><tspan x="191.6" y="173.3">PHYSIC</tspan><tspan x="191.6" y="184.8">INTUITIVE</tspan></text>
    <text class="modality"><tspan x="245.6" y="136">AYURVEDIC</tspan><tspan x="245.6" y="147.5">MEDICINE</tspan></text>
    <text class="modality"><tspan x="306.9" y="112.8">WESTERN</tspan><tspan x="306.9" y="124.3">MEDICINE</tspan></text>

    <!-- centre brand -->
    <circle class="center-mark" cx="372" cy="356" r="17"/>
    <text class="center-name" x="372" y="414">Luminara</text>
  </svg>

  <div class="brand-row">
    <div class="brand-dot"></div>
    <div class="brand-name">KRV</div>
  </div>
  <div class="divider"></div>
  <h1 class="claim">CHOOSE KRV FOR FAST,<br>IMMEDIATE AND POWERFUL RESULTS</h1>

  <ul class="statements">
    <li>I Must Experience Healing On All Levels, I Am Not Just A Body.</li>
    <li>I Want To Learn How To Heal Myself, So I’m Not Dependent On Others.</li>
    <li>I Want To Release All My Emotional And Mental Blocks, So I Can Be The Best Version Of Myself.</li>
  </ul>

  <section class="card physical-card" style="left:74px;top:796px;width:290px;height:92px;">
    <div class="tab"><svg><use href="#icon-physical"/></svg></div>
    <h2>Physical</h2>
    <p>Most modalities, including, a western medicine, focus on and treat the physical body only. The KRV process enables you to engage in healing your own body during the session. There is no muscle testing, no hand-on healing and no herbal remedies or medicines.</p>
  </section>

  <section class="card subconscious-card" style="left:373px;top:796px;width:290px;height:92px;">
    <div class="tab"><svg><use href="#icon-subconscious"/></svg></div>
    <h2>Subconscious</h2>
    <p>Some modalities, like Kinesiology, access your subconscious through muscle testing. KRV empowers you to access your own subconscious and heal it yourself.</p>
  </section>

  <section class="card mental-card" style="left:74px;top:898px;width:290px;height:70px;">
    <div class="tab"><svg><use href="#icon-mental"/></svg></div>
    <h2>Mental</h2>
    <p>KRV enables you to use your own consciousness to self-heal. We don’t give you advice or coaching, we allow your mind to heal itself.</p>
  </section>

  <section class="card superconscious-card" style="left:373px;top:898px;width:290px;height:70px;">
    <div class="tab"><svg><use href="#icon-superconscious"/></svg></div>
    <h2>Superconscious</h2>
    <p>KRV is the only modality that enables you to access and heal your superconscious<br>mind yourself.</p>
  </section>

  <section class="card emotional-card" style="left:74px;top:979px;width:290px;height:81px;">
    <div class="tab"><svg><use href="#icon-emotional"/></svg></div>
    <h2>Emotional</h2>
    <p>KRV is the only modality that engages your emotions on a physical level. Emotions get stuck in your body and can cause illness over time if left unchecked. KRV enables you to experience fast and powerful emotional releasing.</p>
  </section>

  <section class="card testing-card" style="left:373px;top:979px;width:290px;height:81px;">
    <div class="tab"><svg><use href="#icon-testing"/></svg></div>
    <h2 class="compact">Before &amp; After Testing</h2>
    <p>KRV is the only modality that enables you to provide before and after results, which are documented by us, and analyzed by you with our help.</p>
  </section>

  <section class="card energetic-card" style="left:74px;top:1073px;width:290px;height:69px;">
    <div class="tab"><svg><use href="#icon-energetic"/></svg></div>
    <h2>Energetic</h2>
    <p>Most modalities try to move the energy in your body for you. KRV enables and empowers you to do it yourself.</p>
  </section>

  <section class="card contact-card" style="left:373px;top:1073px;width:290px;height:69px;">
    <div class="contact-brand"><div class="contact-dot"></div><div class="contact-name">Luminara</div></div>
    <div class="web">www.luminara.com.au</div>
  </section>
</div>
</body>
</html>
```